Here is the link where the current banner is featured https://www.brimkit.com.au/collections/gel-blasters

I need the banner recreated into desktop and mobile format size.
Update the key points to:
- FREE SHIPPING AUSTRALIA WIDE
- SAME DAY DISPATCH
- BEST PRICE GUARANTEE
- 3000+ 5 STAR REVIEWS
- BEST SERVICE & WARRANTY
- 100% SECURE CHECKOUT

I want the banner to suit the style of the website and make it look better than the last graphic.

I also need the "save even more" picture to be recreated as it looks very plain at the moment,

```html
<!DOCTYPE html>
<html lang="en">
<head>
<meta charset="utf-8">
<title>Brim Kit – Key Points &amp; Save Even More Banners</title>
<link href="https://fonts.googleapis.com/css2?family=Poppins:wght@300;400;600;700;800&display=swap" rel="stylesheet">
<style>
  :root {
    --page-bg: #d6d6d6;
    --panel-dark: #1c1c1e;
    --row-dark: #18181a;
    --brand-red: #e31c23;
    --brand-red-deep: #a5131a;
    --text-white: #ffffff;
    --photo-tone-a: #4a5566;
    --photo-tone-b: #2a2f38;
  }
  * { margin: 0; padding: 0; box-sizing: border-box; }
  html, body {
    width: 1200px; height: 1200px; overflow: hidden;
    background: var(--page-bg);
    font-family: "Poppins", sans-serif;
  }
  .canvas {
    position: relative; width: 1200px; height: 1200px;
    display: flex; flex-direction: column; align-items: center;
    padding-top: 56px; gap: 54px;
  }
  .key-points-banner { width: 900px; height: 576px; display: block; box-shadow: 0 18px 24px -14px rgba(0,0,0,.45); }
  .save-more-banner { width: 728px; height: 392px; display: block; filter: drop-shadow(0 14px 12px rgba(0,0,0,.35)); }
  .point-label { font-family: "Poppins", sans-serif; font-weight: 700; font-size: 15.5px; text-anchor: middle; letter-spacing: -0.2px; }
  .point-label .top { fill: var(--text-white); }
  .point-label .bottom { fill: var(--brand-red); }
  .badge-ring { fill: none; stroke: var(--text-white); }
  .badge-core { fill: var(--text-white); }
  .badge-glyph { fill: var(--panel-dark); }
  .divider { stroke: var(--brand-red); stroke-width: 2; }
  .save-title { font-family: "Poppins", sans-serif; font-weight: 800; font-size: 43px; fill: var(--text-white); text-anchor: middle; }
  .tier-order { font-family: "Poppins", sans-serif; font-weight: 300; font-size: 42px; fill: var(--text-white); }
  .tier-get { font-family: "Poppins", sans-serif; font-weight: 400; font-size: 42px; fill: var(--text-white); }
  .tier-get .amount { font-weight: 800; }
</style>
</head>
<body>
<main class="canvas">

  <!-- Key points banner -->
  <svg class="key-points-banner" viewBox="0 0 855 547" xmlns="http://www.w3.org/2000/svg">
    <defs>
      <radialGradient id="soldierTone" cx="0.62" cy="0.62" r="0.55">
        <stop offset="0" stop-color="var(--photo-tone-a)" stop-opacity="0.85"/>
        <stop offset="0.55" stop-color="var(--photo-tone-b)" stop-opacity="0.7"/>
        <stop offset="1" stop-color="#1c1c1e" stop-opacity="0"/>
      </radialGradient>
    </defs>
    <rect width="855" height="547" fill="var(--panel-dark)"/>
    <rect class="hero-photo" x="360" y="230" width="495" height="317" fill="url(#soldierTone)" role="img" aria-label="Photo of a soldier in tactical gear aiming a rifle through smoke"/>

    <!-- dividers -->
    <line class="divider" x1="244" y1="95" x2="244" y2="247"/>
    <line class="divider" x1="430" y1="95" x2="430" y2="247"/>
    <line class="divider" x1="615" y1="95" x2="615" y2="247"/>
    <line class="divider" x1="242" y1="314" x2="242" y2="467"/>

    <!-- badge: free shipping (pin) -->
    <g transform="translate(145,142)">
      <circle class="badge-ring" r="48" stroke-width="2"/><circle class="badge-ring" r="40" stroke-width="1"/>
      <circle class="badge-core" r="31"/>
      <path class="badge-glyph" d="M0 -19a12 12 0 0 1 12 12c0 9-12 22-12 22s-12-13-12-22a12 12 0 0 1 12-12z"/>
      <circle r="4.5" fill="#fff"/>
    </g>
    <!-- badge: same day dispatch (truck) -->
    <g transform="translate(337,142)">
      <circle class="badge-ring" r="48" stroke-width="2"/><circle class="badge-ring" r="40" stroke-width="1"/>
      <circle class="badge-core" r="31"/>
      <rect class="badge-glyph" x="-16" y="-10" width="20" height="16"/>
      <path class="badge-glyph" d="M6 -5h7l5 6v5h-12z"/>
      <circle class="badge-glyph" cx="-9" cy="9" r="4"/><circle class="badge-glyph" cx="11" cy="9" r="4"/>
      <rect class="badge-glyph" x="-24" y="-6" width="6" height="2"/><rect class="badge-glyph" x="-26" y="0" width="8" height="2"/>
    </g>
    <!-- badge: best price (dollar) -->
    <g transform="translate(522,142)">
      <circle class="badge-ring" r="48" stroke-width="2"/><circle class="badge-ring" r="40" stroke-width="1"/>
      <circle class="badge-core" r="31"/>
      <circle class="badge-glyph" r="19"/>
      <text y="8" text-anchor="middle" font-family="Poppins, sans-serif" font-weight="700" font-size="22" fill="#fff">$</text>
    </g>
    <!-- badge: reviews (star) -->
    <g transform="translate(707,142)">
      <circle class="badge-ring" r="48" stroke-width="2"/><circle class="badge-ring" r="40" stroke-width="1"/>
      <circle class="badge-core" r="31"/>
      <path class="badge-glyph" d="M0 -20l6 12.5 13.5 1.8-9.8 9.4 2.4 13.5L0 10.6l-12.1 6.6 2.4-13.5-9.8-9.4 13.5-1.8z"/>
    </g>
    <!-- badge: service & warranty (gear tick) -->
    <g transform="translate(142,362)">
      <circle class="badge-ring" r="48" stroke-width="2"/><circle class="badge-ring" r="40" stroke-width="1"/>
      <circle class="badge-core" r="31"/>
      <circle class="badge-glyph" r="16"/>
      <g class="badge-glyph">
        <rect x="-4" y="-22" width="8" height="8"/><rect x="-4" y="14" width="8" height="8"/>
        <rect x="-22" y="-4" width="8" height="8"/><rect x="14" y="-4" width="8" height="8"/>
      </g>
      <circle r="10" fill="#fff"/>
      <path d="M-5 0l3.5 3.5 6.5-7" fill="none" stroke="var(--panel-dark)" stroke-width="2.6"/>
    </g>
    <!-- badge: secure checkout (shield tick) -->
    <g transform="translate(327,362)">
      <circle class="badge-ring" r="48" stroke-width="2"/><circle class="badge-ring" r="40" stroke-width="1"/>
      <circle class="badge-core" r="31"/>
      <path class="badge-glyph" d="M0 -20l16 6v9c0 12-7 19-16 24-9-5-16-12-16-24v-9z"/>
      <circle r="8" fill="none" stroke="#fff" stroke-width="1.8"/>
      <path d="M-4 0l3 3 5-6" fill="none" stroke="#fff" stroke-width="2"/>
    </g>

    <!-- labels -->
    <text class="point-label" x="152"><tspan class="top" x="152" y="230">FREE SHIPPING</tspan><tspan class="bottom" x="152" y="248">AUSTRALIA WIDE</tspan></text>
    <text class="point-label"><tspan class="top" x="337" y="230">SAME DAY</tspan><tspan class="bottom" x="337" y="248">DISPATCH</tspan></text>
    <text class="point-label"><tspan class="top" x="522" y="230">BEST PRICE</tspan><tspan class="bottom" x="522" y="248">GUARANTEE</tspan></text>
    <text class="point-label"><tspan class="top" x="707" y="230">3000+ 5 STAR</tspan><tspan class="bottom" x="707" y="248">REVIEWS</tspan></text>
    <text class="point-label"><tspan class="top" x="149" y="450">BEST SERVICE &amp;</tspan><tspan class="bottom" x="149" y="468">WARRANTY</tspan></text>
    <text class="point-label"><tspan class="top" x="334" y="450">100% SECURE</tspan><tspan class="bottom" x="334" y="468">CHECKOUT</tspan></text>
  </svg>

  <!-- Save even more banner -->
  <svg class="save-more-banner" viewBox="0 0 692 372" xmlns="http://www.w3.org/2000/svg">
    <rect y="22" width="692" height="350" fill="var(--panel-dark)"/>
    <!-- title ribbon -->
    <path d="M32 22L46 0h14z" fill="var(--brand-red-deep)"/>
    <path d="M660 22L646 0h-14z" fill="var(--brand-red-deep)"/>
    <path d="M46 0H646L606 72q-4 6-12 6H98q-8 0-12-6z" fill="var(--brand-red)"/>
    <text class="save-title" x="346" y="55">SAVE EVEN MORE</text>

    <!-- tier rows -->
    <g class="tier">
      <rect x="0" y="97" width="692" height="67" fill="var(--row-dark)"/>
      <path d="M372 97H692V164H350z" fill="var(--brand-red)"/>
      <rect x="0" y="163" width="692" height="3" fill="var(--brand-red)"/>
      <text class="tier-order" x="42" y="147">ORDER $250+</text>
      <text class="tier-get" x="380" y="148">GET <tspan class="amount">5% OFF</tspan></text>
    </g>
    <g class="tier">
      <rect x="0" y="184" width="692" height="67" fill="var(--row-dark)"/>
      <path d="M372 184H692V251H350z" fill="var(--brand-red)"/>
      <rect x="0" y="250" width="692" height="3" fill="var(--brand-red)"/>
      <text class="tier-order" x="42" y="234">ORDER $500+</text>
      <text class="tier-get" x="380" y="235">GET <tspan class="amount">10% OFF</tspan></text>
    </g>
    <g class="tier">
      <rect x="0" y="270" width="692" height="67" fill="var(--row-dark)"/>
      <path d="M372 270H692V337H350z" fill="var(--brand-red)"/>
      <rect x="0" y="336" width="692" height="3" fill="var(--brand-red)"/>
      <text class="tier-order" x="42" y="320">ORDER $1000+</text>
      <text class="tier-get" x="380" y="321">GET <tspan class="amount">15% OFF</tspan></text>
    </g>
  </svg>

</main>
</body>
</html>
```